Bottle label design for a mulberry brandy

Please create a label design for a mulberry brandy. The registered brand name is "Kolvat"
The brandy will be produced in Armenia from 100% mulberry.
Color of the product: transparent.
The product will be sold worldwide. The price will be between 30 and 50 USD. So the product will be in premium category.
Therefore we need a solid design, appropriate to the product price category. The design, however, needs to be modern and optimistic.
You can have mulberries on the label or not have, it is up to you.
We have chosen for the product some bottle types, the links to the available bottles you can find in the attachment. Ideally you show a picture of your label on the bottle you selected.

Target Market(s)

worldwide

```html
<!DOCTYPE html>
<html lang="en">
<head>
<meta charset="utf-8">
<title>Kolvat Mulberry Brandy – Label</title>
<link rel="stylesheet" href="https://fonts.googleapis.com/css2?family=Bodoni+Moda:wght@700&family=Pinyon+Script&family=Josefin+Sans:wght@400&display=swap">
<style>
  :root {
    --page: #ffffff;
    --label-light: #f7f7f4;
    --label-mid: #ecebe7;
    --label-dark: #d3d4d1;
    --ink: #0d0d0d;
    --slate: #4a5664;
    --slate-soft: #9aa6b3;
    --gold: #b8963a;
    --dot: #c4c8cc;
  }
  * { margin: 0; padding: 0; box-sizing: border-box; }
  html, body {
    width: 913px;
    height: 1200px;
    overflow: hidden;
    background: var(--page);
  }
  .label {
    position: absolute;
    left: 46px;
    top: 290px;
    width: 820px;
    height: 621px;
    background: linear-gradient(90deg, var(--label-light) 0%, var(--label-mid) 55%, var(--label-dark) 100%);
  }
  .label__botanical {
    position: absolute;
    left: 253px;
    top: 0;
    width: 316px;
    height: 390px;
    background: radial-gradient(ellipse at 45% 50%, rgba(154,166,179,0.55) 0%, rgba(154,166,179,0.25) 50%, rgba(154,166,179,0) 75%);
  }
  .label__brand {
    position: absolute;
    left: 395px;
    top: 48px;
    height: 405px;
    width: 60px;
    writing-mode: vertical-rl;
    transform: rotate(180deg);
    font-family: "Bodoni Moda", serif;
    font-weight: 700;
    font-size: 58px;
    line-height: 60px;
    letter-spacing: 16px;
    text-transform: uppercase;
    text-align: center;
    color: var(--ink);
  }
  .label__origin {
    position: absolute;
    left: 0;
    width: 820px;
    top: 478px;
    padding-left: 12px;
    text-align: center;
    font-family: "Pinyon Script", cursive;
    font-size: 30px;
    color: var(--gold);
  }
  .label__row {
    position: absolute;
    left: 0;
    top: 566px;
    width: 820px;
    font-family: "Josefin Sans", sans-serif;
    font-size: 17px;
    letter-spacing: 4px;
    color: var(--slate);
  }
  .label__abv { position: absolute; left: 57px; top: 0; }
  .label__volume { position: absolute; left: 664px; top: 0; }
  .label__type {
    position: absolute;
    left: 245px;
    width: 340px;
    top: 0;
    text-align: center;
    font-size: 19px;
  }
  .label__dots {
    position: absolute;
    left: 265px;
    width: 300px;
    height: 0;
    border-top: 2px dotted var(--dot);
  }
  .label__dots--top { top: 552px; }
  .label__dots--bottom { top: 598px; }
</style>
</head>
<body>
  <div class="label">
    <div class="label__botanical" role="img" aria-label="Engraved botanical drawing of a mulberry branch with leaves and catkins"></div>
    <div class="label__brand">Kolvat</div>
    <div class="label__origin">Produced in Armenia</div>
    <div class="label__dots label__dots--top"></div>
    <div class="label__row">
      <span class="label__abv">40% VOL.</span>
      <span class="label__type">MULBERRY BRANDY</span>
      <span class="label__volume">750ML.</span>
    </div>
    <div class="label__dots label__dots--bottom"></div>
  </div>
</body>
</html>
```